Digital Transformation Company Template Slidedeck

I am looking for help designing a set of standard business powerpoint slides that are branded specifically for my company. I have attached more details and the logo design file that can be used for this project. Thanks!

Target Market(s)

Small and Medium Businesses

```html
<!DOCTYPE html>
<html lang="en">
<head>
<meta charset="utf-8">
<title>Voltrix Slide Deck Overview</title>
<link href="https://fonts.googleapis.com/css2?family=Montserrat:wght@300;400;500;600;700&display=swap" rel="stylesheet">
<style>
:root{
  --orange:#e8651f;
  --blue:#2f8fe6;
  --slate:#8fa3b5;
  --slate-dark:#6d8097;
  --ink:#222;
  --muted:#9a9a9a;
  --shadow:0 8px 22px rgba(0,0,0,.2);
  --band:linear-gradient(180deg,#eb6a1f 0%,#c8788a 55%,#3390e8 100%);
}
*{margin:0;padding:0;box-sizing:border-box}
html,body{width:1200px;height:1200px;overflow:hidden;background:#fff}
body{font-family:'Montserrat',sans-serif;color:var(--ink)}
.sheet{position:absolute;left:0;top:0;width:1920px;height:1920px;transform:scale(.625);transform-origin:0 0}
.slide{position:absolute;width:468px;height:264px;background:#fff;box-shadow:var(--shadow);overflow:hidden}
.abs{position:absolute}
.brand{position:absolute;left:37px;top:20px;font-weight:700;font-size:7px;letter-spacing:.6px;color:var(--orange)}
.dots{position:absolute;right:32px;top:26px;display:flex;gap:4px}
.dots i{width:3px;height:3px;border-radius:50%;background:var(--blue)}
.dots i:last-child{background:var(--orange)}
.foot{position:absolute;left:37px;bottom:9px;font-size:4.4px;color:#888}
.foot b{font-weight:400;color:var(--orange)}
.url{position:absolute;right:37px;bottom:9px;font-size:4.4px;color:#888}
.kicker{font-size:5px;color:var(--blue);letter-spacing:.3px}
.title{font-size:16px;font-weight:400;line-height:1.15;color:var(--ink)}
.title .o{color:var(--orange)}
.copy{font-size:4.8px;line-height:1.95;color:var(--muted)}
.label{font-size:7px;color:var(--ink);line-height:1.2}
.band{position:absolute;background:var(--band)}
.photo{position:absolute;background:linear-gradient(160deg,#c9c2b8,#8d8f96 60%,#5b6470)}
.photo.warm{background:linear-gradient(150deg,#d9c2a3,#a38a72 55%,#6e6a6a)}
.photo.cool{background:linear-gradient(150deg,#dfe3e8,#9aa7b4 55%,#56606c)}
.photo.dark{background:linear-gradient(160deg,#5b7a6a,#2f3e48 60%,#1f2a33)}
.framed{outline:2px solid #fff}
</style>
</head>
<body>
<div class="sheet">

<!-- Row 1 -->
<section class="slide" style="left:124px;top:74px">
  <div class="photo warm" role="img" aria-label="Team of professionals collaborating in an office" style="inset:0;opacity:.55"></div>
  <div class="abs" style="inset:0;background:rgba(255,255,255,.55)"></div>
  <div class="abs" style="left:40px;top:87px;width:90px;height:90px;border-radius:50%;background:#2a2a2a;display:flex;align-items:center;justify-content:center;font-weight:700;font-size:12px;letter-spacing:1px;color:var(--orange)">VOLTRIX</div>
  <div class="abs" style="left:163px;top:88px;font-size:26px;font-weight:300;letter-spacing:4px;line-height:1.24;color:#2a2a2a;text-align:right">LOOKING TO<br>THRIVE THE<br>DIGITAL AGE</div>
  <div class="abs" style="left:428px;top:111px;display:flex;flex-direction:column;gap:7px">
    <i style="width:4px;height:4px;border-radius:50%;background:var(--orange)"></i>
    <i style="width:4px;height:4px;border-radius:50%;background:var(--slate)"></i>
    <i style="width:4px;height:4px;border-radius:50%;background:var(--blue)"></i>
  </div>
  <div class="abs" style="left:200px;top:236px;font-size:6.5px;color:#333">www.voltrix.io</div>
  <div class="foot">Copyright © 2021 Voltrix Technology, LLC. All Rights Reserved.</div>
  <div class="url">www.voltrix.io | 1</div>
</section>

<section class="slide" style="left:732px;top:74px">
  <div class="brand">VOLTRIX</div>
  <div class="dots"><i></i><i></i><i></i></div>
  <div class="abs kicker" style="left:37px;top:50px;color:var(--orange)">TODAY PRESENTATION</div>
  <div class="abs title" style="left:37px;top:57px">PAGE OF <span class="o">CONTENT</span></div>
  <p class="abs copy" style="left:37px;top:81px;width:380px">Lorem ipsum dolor sit amet, consectetuer adipiscing elit. Aenean commodo ligula eget dolor. Aenean massa. Cum sociis natoque penatibus et magnis dis parturient montes, nascetur ridiculus mus. Donec quam felis, ultricies nec, pellentesque eu, pretium quis, sem.</p>
  <div class="abs" style="left:58px;top:137px;font-size:5.5px;line-height:19px;color:var(--ink)">
    <div><span style="color:var(--orange);margin-right:10px">01</span>Message From The President</div>
    <div><span style="color:var(--orange);margin-right:10px">02</span>Company Growth</div>
    <div><span style="color:var(--orange);margin-right:10px">03</span>Global Market</div>
    <div><span style="color:var(--orange);margin-right:10px">04</span>Service</div>
  </div>
  <div class="abs" style="left:257px;top:137px;font-size:5.5px;line-height:19px;color:var(--ink)">
    <div><span style="color:var(--orange);margin-right:10px">05</span>Board of Directors</div>
    <div><span style="color:var(--orange);margin-right:10px">06</span>Company Structure</div>
    <div><span style="color:var(--orange);margin-right:10px">07</span>Sales Report</div>
    <div><span style="color:var(--orange);margin-right:10px">08</span>Promotion Strategy</div>
  </div>
  <div class="foot">Copyright © 2021 <b>Voltrix Technology, LLC.</b> All Rights Reserved.</div>
  <div class="url">www.voltrix.io | 2</div>
</section>

<section class="slide" style="left:1340px;top:74px">
  <div class="brand">VOLTRIX</div>
  <div class="dots"><i></i><i></i><i></i></div>
  <div class="band" style="left:265px;top:0;width:105px;height:264px"></div>
  <div class="photo warm framed" role="img" aria-label="Woman with glasses working at a laptop beside a colleague" style="left:233px;top:25px;width:108px;height:142px"></div>
  <div class="photo dark framed" role="img" aria-label="Computer screens showing code" style="left:340px;top:96px;width:62px;height:134px"></div>
  <div class="abs kicker" style="left:36px;top:81px">DIGITAL TRANSFORMATION</div>
  <div class="abs title" style="left:36px;top:93px">LOOKING TO THRIVE<br><span class="o">THE DIGITAL AGE</span></div>
  <p class="abs copy" style="left:36px;top:140px;width:186px;text-align:justify">Lorem ipsum dolor sit amet, consectetuer adipiscing elit. Aenean commodo ligula eget dolor. Aenean massa. Cum sociis natoque penatibus et magnis dis parturient montes, nascetur ridiculus mus. Donec quam felis, ultricies nec, pellentesque eu, pretium quis, sem.</p>
  <div class="foot">Copyright © 2021 Voltrix Technology, LLC. All Rights Reserved.</div>
  <div class="url">www.voltrix.io | 3</div>
</section>

<!-- Row 2 -->
<section class="slide" style="left:124px;top:378px">
  <div class="brand">VOLTRIX</div>
  <div class="dots"><i></i><i></i><i></i></div>
  <div class="abs kicker" style="left:39px;top:51px">DIGITAL TRANSFORMATION</div>
  <div class="abs title" style="left:39px;top:61px">WHY<br><span class="o">CHOOSE US</span></div>
  <p class="abs copy" style="left:39px;top:104px;width:152px">Lorem ipsum dolor sit amet, consectetuer adipiscing elit. Aenean commodo ligula eget dolor. Aenean massa. Cum sociis natoque penatibus et magnis dis parturient montes, nascetur ridiculus mus. Donec quam felis, ultricies nec, pellentesque eu, pretium quis, sem. Nulla consequat massa quis enim. Lorem ipsum dolor sit amet, consectetuer adipiscing elit. Aenean commodo ligula eget dolor. Aenean massa. Cum sociis natoque penatibus et magnis dis parturient montes, nascetur ridiculus mus.</p>
  <div class="abs" style="left:223px;top:51px;width:188px;height:62px;background:var(--orange)">
    <svg class="abs" style="left:14px;top:26px" width="10" height="10" viewBox="0 0 10 10"><rect x="1" y="2" width="8" height="7" fill="#fff"/><rect x="3" y="1" width="4" height="2" fill="#fff"/></svg>
    <div class="abs" style="left:30px;top:0;bottom:0;border-left:1px solid rgba(255,255,255,.6)"></div>
    <div class="abs" style="left:45px;top:9px;font-size:5.8px;color:#fff">Planning</div>
    <div class="abs" style="left:45px;top:20px;width:130px;font-size:4.6px;line-height:1.9;color:#fff">Lorem ipsum dolor sit amet, consectetuer adipiscing elit. Aenean commodo ligula.</div>
  </div>
  <div class="abs" style="left:259px;top:120px;height:46px;border-left:1px solid #ccc"></div>
  <div class="abs" style="left:259px;top:178px;height:48px;border-left:1px solid #ccc"></div>
  <svg class="abs" style="left:238px;top:138px" width="11" height="12" viewBox="0 0 11 12"><rect x="1" y="1" width="9" height="10" fill="none" stroke="#333" stroke-width="1.2"/><path d="M3 4h5M3 6h5M3 8h5" stroke="#333"/></svg>
  <svg class="abs" style="left:237px;top:196px" width="12" height="9" viewBox="0 0 12 9"><rect x=".5" y=".5" width="11" height="8" fill="#333"/><path d="M.5 .5l5.5 4.5 5.5-4.5" stroke="#fff" fill="none"/></svg>
  <div class="abs" style="left:268px;top:125px;font-size:5.8px">Status</div>
  <div class="abs copy" style="left:268px;top:134px;width:130px">Lorem ipsum dolor sit amet, consectetuer adipiscing elit. Aenean commodo ligula.</div>
  <div class="abs" style="left:268px;top:184px;font-size:5.8px">Contacting</div>
  <div class="abs copy" style="left:268px;top:193px;width:130px">Lorem ipsum dolor sit amet, consectetuer adipiscing elit. Aenean commodo ligula.</div>
  <div class="foot">Copyright © 2021 <b>Voltrix Technology, LLC.</b> All Rights Reserved.</div>
  <div class="url">www.voltrix.io | 4</div>
</section>

<section class="slide" style="left:732px;top:378px">
  <div class="brand">VOLTRIX</div>
  <div class="dots"><i></i><i></i><i></i></div>
  <div class="band" style="left:365px;top:0;width:103px;height:264px"></div>
  <div class="abs" style="left:284px;top:48px;width:104px;height:186px;background:var(--orange)"></div>
  <div class="photo dark framed" role="img" aria-label="Man holding a laptop in front of code screens" style="left:268px;top:60px;width:110px;height:178px"></div>
  <div class="abs kicker" style="left:39px;top:49px">DIGITAL TRANSFORMATION</div>
  <div class="abs title" style="left:39px;top:59px">A MESSAGE<br><span class="o">OUR PRESIDENT</span></div>
  <p class="abs copy" style="left:39px;top:104px;width:190px;text-align:justify">Lorem ipsum dolor sit amet, consectetuer adipiscing elit. Aenean commodo ligula eget dolor. Aenean massa. Cum sociis natoque penatibus et magnis dis parturient montes, nascetur ridiculus mus. Donec quam felis, ultricies nec, pellentesque eu, pretium quis, sem. Nulla consequat massa quis enim. Lorem ipsum dolor sit amet, consectetuer adipiscing elit. Aenean commodo ligula eget dolor. Aenean massa. Cum sociis natoque penatibus et magnis dis parturient montes, nascetur ridiculus mus.</p>
  <div class="abs" style="left:174px;top:208px;font-size:5.8px">Marco Ellison</div>
  <div class="abs" style="left:174px;top:216px;font-size:3.8px;font-style:italic;color:var(--muted)">President Management</div>
  <div class="foot">Copyright © 2021 <b>Voltrix Technology, LLC.</b> All Rights Reserved.</div>
</section>

<section class="slide" style="left:1340px;top:378px">
  <div class="brand">VOLTRIX</div>
  <div class="dots"><i></i><i></i><i></i></div>
  <div class="abs title" style="left:0;right:0;top:19px;text-align:center;font-size:14.5px">BUSINESS <span class="o">MODEL</span></div>
  <p class="abs copy" style="left:37px;top:48px;width:395px">Lorem ipsum dolor sit amet, consectetuer adipiscing elit. Aenean commodo ligula eget dolor. Aenean massa. Cum sociis natoque penatibus et magnis dis parturient montes, nascetur ridiculus mus. Donec quam felis, ultricies nec, pellentesque eu, pretium quis, sem. Nulla consequat massa quis enim. Lorem ipsum dolor sit amet, consectetuer adipiscing elit. Aenean commodo ligula eget dolor. Aenean massa. Cum sociis natoque penatibus et magnis dis parturient montes, nascetur ridiculus mus.</p>
  <div class="abs" style="left:75px;top:108px;width:88px;height:122px;background:var(--orange);color:#fff;text-align:center">
    <svg style="margin-top:16px" width="9" height="9" viewBox="0 0 9 9"><rect x=".5" y=".5" width="8" height="8" fill="none" stroke="#fff"/><path d="M2 6l4-4" stroke="#fff"/></svg>
    <div style="font-size:5.8px;margin-top:12px">Planning</div>
    <div style="font-size:4.2px;line-height:1.9;margin:6px 12px 0">Lorem ipsum dolor sit amet, consectetuer adipiscing elit</div>
    <div style="font-size:4.2px;border:1px solid #fff;margin:8px 24px 0">More</div>
  </div>
  <div class="abs" style="left:190px;top:108px;width:88px;height:122px;background:var(--blue);color:#fff;text-align:center">
    <svg style="margin-top:16px" width="9" height="9" viewBox="0 0 9 9"><path d="M4.5 .5l4 2v4l-4 2-4-2v-4z" fill="#fff"/></svg>
    <div style="font-size:5.8px;margin-top:12px">Production</div>
    <div style="font-size:4.2px;line-height:1.9;margin:6px 12px 0">Lorem ipsum dolor sit amet, consectetuer adipiscing elit.</div>
    <div style="font-size:4.2px;border:1px solid #fff;margin:8px 24px 0">More</div>
  </div>
  <div class="abs" style="left:302px;top:108px;width:88px;height:122px;background:var(--slate);color:#fff;text-align:center">
    <svg style="margin-top:16px" width="9" height="9" viewBox="0 0 9 9"><rect x="1.5" y=".5" width="6" height="8" fill="none" stroke="#fff"/><path d="M3 3h3M3 5h3" stroke="#fff"/></svg>
    <div style="font-size:5.8px;margin-top:12px">Marketing</div>
    <div style="font-size:4.2px;line-height:1.9;margin:6px 12px 0">Lorem ipsum dolor sit amet, consectetuer adipiscing elit.</div>
    <div style="font-size:4.2px;border:1px solid #fff;margin:8px 24px 0">More</div>
  </div>
  <div class="foot">Copyright © 2021 <b>Voltrix Technology, LLC.</b> All Rights Reserved.</div>
  <div class="url">www.voltrix.io | 6</div>
</section>

<!-- Row 3 -->
<section class="slide" style="left:124px;top:682px">
  <div class="dots"><i></i><i></i><i></i></div>
  <div class="band" style="left:59px;top:0;width:63px;height:264px"></div>
  <div class="photo warm" role="img" aria-label="Smiling woman with glasses using a laptop" style="left:120px;top:0;width:115px;height:264px"></div>
  <div class="abs kicker" style="left:271px;top:40px">DIGITAL TRANSFORMATION</div>
  <div class="abs title" style="left:271px;top:49px">OUR <span class="o">VISION</span></div>
  <div class="abs" style="left:271px;top:78px;font-size:6px">Vision One</div>
  <div class="abs copy" style="left:271px;top:87px;width:130px">Lorem ipsum dolor sit amet, consectetuer adipiscing elit. Aenean commodo ligula.</div>
  <div class="abs" style="left:271px;top:133px;font-size:6px">Vision Two</div>
  <div class="abs copy" style="left:271px;top:142px;width:130px">Lorem ipsum dolor sit amet, consectetuer adipiscing elit. Aenean commodo ligula.</div>
  <div class="abs" style="left:271px;top:192px;font-size:6px">Vision Three</div>
  <div class="abs copy" style="left:271px;top:201px;width:130px">Lorem ipsum dolor sit amet, consectetuer adipiscing elit. Aenean commodo ligula.</div>
  <div class="foot">Copyright</div>
  <div class="url">www.voltrix.io | 7</div>
</section>

<section class="slide" style="left:732px;top:682px">
  <div class="brand">VOLTRIX</div>
  <div class="dots"><i></i><i></i><i></i></div>
  <div class="band" style="left:365px;top:0;width:103px;height:264px"></div>
  <div class="photo cool framed" role="img" aria-label="Woman writing on a whiteboard" style="left:268px;top:62px;width:107px;height:176px"></div>
  <div class="abs kicker" style="left:37px;top:49px">DIGITAL TRANSFORMATION</div>
  <div class="abs title" style="left:37px;top:64px">COMPANY<br><span class="o">PROFILE</span></div>
  <svg class="abs" style="left:37px;top:114px" width="12" height="11" viewBox="0 0 12 11"><path d="M6 0l6 3H0z" fill="#333"/><path d="M2 4v5M5 4v5M7 4v5M10 4v5" stroke="#333"/><rect x="0" y="9.5" width="12" height="1.5" fill="#333"/></svg>
  <svg class="abs" style="left:149px;top:114px" width="11" height="12" viewBox="0 0 11 12"><circle cx="5.5" cy="4.5" r="3.6" fill="none" stroke="#333" stroke-width="1.2"/><path d="M3 8l-1 4 3.5-1.6L9 12 8 8" fill="none" stroke="#333"/></svg>
  <div class="abs label" style="left:37px;top:136px;width:100px">We Are The First World Company</div>
  <div class="abs label" style="left:151px;top:136px;width:100px">We Are The First Company Of The World</div>
  <div class="abs copy" style="left:37px;top:162px;width:98px">Lorem ipsum dolor sit amet,leg bvsc consectetuer adipiscing elit. Aenean commodo ligula eget</div>
  <div class="abs copy" style="left:151px;top:162px;width:98px">Lorem ipsum dolor sit amet,leg bvsc consectetuer adipiscing elit. Aenean commodo ligula eget</div>
  <div class="foot">Copyright © 2021 <b>Voltrix Technology, LLC.</b> All Rights Reserved.</div>
</section>

<section class="slide" style="left:1340px;top:682px">
  <div class="brand">VOLTRIX</div>
  <div class="dots"><i></i><i></i><i></i></div>
  <div class="photo cool" role="img" aria-label="Team working on laptops around a long table" style="left:196px;top:37px;width:240px;height:94px"></div>
  <div class="abs kicker" style="left:37px;top:51px">DIGITAL TRANSFORMATION</div>
  <div class="abs title" style="left:37px;top:58px">OUR <span class="o">MISSION</span></div>
  <div class="abs" style="left:37px;top:82px;width:145px;font-size:5.2px;line-height:1.9;color:#333">Lorem ipsum dolor sit amet, consectetuer adipiscing elit. Aenean commodo ligula eget dolor. Aenean massa. Cum sociis natoque penatibus et magnis dis</div>
  <div class="abs" style="left:38px;top:155px;font-size:6px">Mission One</div>
  <div class="abs copy" style="left:38px;top:164px;width:122px">Lorem ipsum dolor sit amet, consectetuer adipiscing elit. Aenean commodo ligula eget dolor. Aenean massa. Cum sociis natoque penatibus et magnis dis parturient montes, nascetur ridiculus</div>
  <div class="abs" style="left:174px;top:154px;font-size:6px">Mission Two</div>
  <div class="abs copy" style="left:174px;top:163px;width:122px">Lorem ipsum dolor sit amet, consectetuer adipiscing elit. Aenean commodo ligula eget dolor. Aenean massa. Cum sociis natoque penatibus et magnis dis parturient montes, nascetur ridiculus</div>
  <div class="abs" style="left:310px;top:154px;font-size:6px">Mission Three</div>
  <div class="abs copy" style="left:310px;top:163px;width:122px">Lorem ipsum dolor sit amet, consectetuer adipiscing elit. Aenean commodo ligula eget dolor. Aenean massa. Cum sociis natoque penatibus et magnis dis parturient montes, nascetur ridiculus</div>
  <div class="foot">Copyright © 2021 <b>Voltrix Technology, LLC.</b> All Rights Reserved.</div>
  <div class="url">www.voltrix.io | 9</div>
</section>

<!-- Row 4 -->
<section class="slide" style="left:124px;top:986px">
  <div class="brand">VOLTRIX</div>
  <div class="dots"><i></i><i></i><i></i></div>
  <div class="band" style="left:365px;top:0;width:103px;height:264px"></div>
  <div class="abs kicker" style="left:38px;top:51px">DIGITAL TRANSFORMATION</div>
  <div class="abs title" style="left:38px;top:60px">OUR <span class="o">SERVICE</span></div>
  <svg class="abs" style="left:35px;top:107px" width="12" height="12" viewBox="0 0 12 12"><rect x="1" y="2" width="10" height="9" fill="var(--orange)"/><path d="M1 5h10M4 5v6M8 5v6" stroke="#fff"/></svg>
  <svg class="abs" style="left:121px;top:106px" width="12" height="13" viewBox="0 0 12 13"><path d="M6 1l4 3-4 8-4-8z" fill="none" stroke="var(--orange)" stroke-width="1.4"/></svg>
  <svg class="abs" style="left:207px;top:107px" width="11" height="12" viewBox="0 0 11 12"><rect x="1" y="1" width="9" height="10" rx="1" fill="var(--orange)"/><rect x="3" y="2" width="5" height="3" fill="#fff"/></svg>
  <svg class="abs" style="left:293px;top:106px" width="13" height="13" viewBox="0 0 13 13"><rect x="2" y="1" width="8" height="10" fill="none" stroke="var(--orange)" stroke-width="1.2"/><circle cx="9" cy="9" r="3" fill="var(--orange)"/></svg>
  <div class="abs label" style="left:35px;top:128px;width:70px">Provide<br>Warranty</div>
  <div class="abs label" style="left:121px;top:128px;width:70px">Service<br>Ptovided</div>
  <div class="abs label" style="left:207px;top:128px;width:70px">Backup Data<br>Phone</div>
  <div class="abs label" style="left:293px;top:128px;width:70px">Free Software<br>Installation</div>
  <div class="abs copy" style="left:35px;top:148px;width:66px;text-align:justify">Lorem ipsum dolor sit amet, consectetuer adipiscing elit. Aenean commodo ligula eget dolor. Aenean massa. Cum sociis natoque penatibus</div>
  <div class="abs copy" style="left:121px;top:148px;width:66px;text-align:justify">Lorem ipsum dolor sit amet, consectetuer adipiscing elit. Aenean commodo ligula eget dolor. Aenean massa. Cum sociis natoque penatibus</div>
  <div class="abs copy" style="left:207px;top:148px;width:66px;text-align:justify">Lorem ipsum dolor sit amet, consectetuer adipiscing elit. Aenean commodo ligula eget dolor. Aenean massa. Cum sociis natoque penatibus</div>
  <div class="abs copy" style="left:293px;top:148px;width:66px;text-align:justify">Lorem ipsum dolor sit amet, consectetuer adipiscing elit. Aenean commodo ligula eget dolor. Aenean massa. Cum sociis natoque penatibus</div>
  <div class="foot">Copyright © 2021 <b>Voltrix Technology, LLC.</b> All Rights Reserved.</div>
  <div class="url" style="color:#fff;right:48px">www.voltrix.io</div>
</section>

<section class="slide" style="left:732px;top:986px">
  <div class="dots"><i></i><i></i><i></i></div>
  <div class="abs" style="left:30px;top:0;width:103px;height:180px;background:var(--orange)"></div>
  <div class="abs" style="left:30px;top:150px;width:30px;height:30px;background:var(--blue)"></div>
  <div class="photo dark framed" role="img" aria-label="Company president holding a laptop" style="left:58px;top:24px;width:110px;height:214px"></div>
  <div class="abs title" style="left:200px;top:38px">MEET <span class="o">OUR BOSS</span></div>
  <div class="abs" style="left:202px;top:61px;font-size:5.8px">Marco Ellison</div>
  <div class="abs" style="left:202px;top:69px;font-size:3.8px;font-style:italic;color:var(--muted)">President Management</div>
  <div class="abs" style="left:200px;top:81px;font-size:5.8px">Education &amp; Expererience</div>
  <p class="abs copy" style="left:200px;top:96px;width:200px">Lorem ipsum dolor sit amet, consectetuer adipiscing elit. Aenean commodo ligula eget dolor. Aenean massa. Cum sociis natoque penatibus et magnis dis parturient montes, nascetur ridiculus mus. Donec quam felis, ultricies nec, pellentesque eu, pretium.</p>
  <div class="abs" style="left:200px;top:154px;font-size:5.8px">Capabilities</div>
  <svg class="abs" style="left:200px;top:164px" width="160" height="70" viewBox="0 0 160 70" font-family="Montserrat,sans-serif">
    <g font-size="4.3" fill="#999">
      <text x="0" y="15">Ledership</text><text x="0" y="32">Creativity</text><text x="0" y="49">Ledership</text><text x="0" y="66">Team Work</text>
      <text x="134" y="6">80%</text><text x="134" y="23">70%</text><text x="134" y="40">60%</text><text x="134" y="57">50%</text>
    </g>
    <g fill="#ddd"><rect x="37" y="11" width="114" height="3"/><rect x="37" y="28" width="114" height="3"/><rect x="37" y="45" width="114" height="3"/><rect x="37" y="62" width="114" height="3"/></g>
    <g fill="#1f5ea8"><rect x="37" y="11" width="95" height="3"/><rect x="37" y="28" width="83" height="3"/><rect x="37" y="45" width="72" height="3"/><rect x="37" y="62" width="60" height="3"/></g>
  </svg>
  <div class="foot">Copyright © 2021 <b>Voltrix Technology, LLC.</b> All Rights Reserved.</div>
  <div class="url">www.voltrix.io | 11</div>
</section>

<section class="slide" style="left:1340px;top:986px">
  <div class="photo cool" role="img" aria-label="Colleagues meeting around a table with laptops" style="left:0;top:0;width:468px;height:113px"></div>
  <div class="abs title" style="left:38px;top:146px">WHAT <span class="o">WE DO</span></div>
  <p class="abs copy" style="left:38px;top:172px;width:170px">Lorem ipsum dolor sit amet, consectetuer adipiscing elit. Aenean commodo ligula eget dolor. Aenean massa. Cum sociis natoque penatibus et magnis dis parturient montes, nascetur ridiculus mus. Donec quam felis, ultricies nec, pellentesque eu, pretium quis, sem.</p>
  <svg class="abs" style="left:236px;top:140px" width="18" height="15" viewBox="0 0 18 15"><rect x="2" y="4" width="7" height="6" fill="var(--orange)"/><rect x="9" y="2" width="7" height="7" fill="var(--orange)"/><rect x="5" y="9" width="7" height="6" fill="var(--orange)"/></svg>
  <svg class="abs" style="left:316px;top:141px" width="10" height="14" viewBox="0 0 10 14"><rect x="1" y="1" width="8" height="12" rx="1" fill="none" stroke="var(--orange)" stroke-width="1.4"/></svg>
  <svg class="abs" style="left:390px;top:143px" width="12" height="9" viewBox="0 0 12 9"><rect width="12" height="9" fill="var(--orange)"/><path d="M0 0l6 5 6-5" stroke="#fff" fill="none"/></svg>
  <svg class="abs" style="left:234px;top:198px" width="14" height="12" viewBox="0 0 14 12"><circle cx="5" cy="4" r="3" fill="var(--orange)"/><path d="M0 12c0-4 10-4 10 0z" fill="var(--orange)"/><circle cx="11" cy="3" r="2" fill="var(--orange)"/></svg>
  <svg class="abs" style="left:315px;top:199px" width="13" height="11" viewBox="0 0 13 11"><rect x="1" y="1" width="11" height="7" fill="none" stroke="var(--orange)" stroke-width="1.4"/><path d="M4 10h5" stroke="var(--orange)"/></svg>
  <svg class="abs" style="left:391px;top:197px" width="11" height="13" viewBox="0 0 11 13"><path d="M4 10V2l6-1v8" fill="none" stroke="var(--orange)" stroke-width="1.4"/><circle cx="2.5" cy="10.5" r="2" fill="var(--orange)"/><circle cx="8.5" cy="9" r="2" fill="var(--orange)"/></svg>
  <div class="abs" style="left:236px;top:166px;font-size:5px;line-height:1.2;text-align:center">dolor sit<br>amet</div>
  <div class="abs" style="left:312px;top:166px;font-size:5px;line-height:1.2;text-align:center">dolor sit<br>amet</div>
  <div class="abs" style="left:383px;top:166px;font-size:5px;line-height:1.2;text-align:center">dolor sit<br>amet</div>
  <div class="abs" style="left:234px;top:221px;font-size:5px;line-height:1.2;text-align:center">dolor sit<br>amet</div>
  <div class="abs" style="left:312px;top:221px;font-size:5px;line-height:1.2;text-align:center">dolor sit<br>amet</div>
  <div class="abs" style="left:383px;top:221px;font-size:5px;line-height:1.2;text-align:center">dolor sit<br>amet</div>
  <div class="foot">Copyright © 2021 <b>Voltrix Technology, LLC.</b> All Rights Reserved.</div>
  <div class="url">www.voltrix.io | 12</div>
</section>

<!-- Row 5 -->
<section class="slide" style="left:124px;top:1290px">
  <div class="brand">VOLTRIX</div>
  <div class="dots"><i></i><i></i><i></i></div>
  <div class="abs title" style="left:40px;top:46px;font-size:15px">OUR <span class="o">FEATURE MOBILE</span></div>
  <svg class="abs" style="left:44px;top:87px" width="15" height="9" viewBox="0 0 15 9"><rect width="15" height="9" rx="4.5" fill="var(--orange)"/><path d="M3 4.5h3M4.5 3v3" stroke="#fff"/></svg>
  <svg class="abs" style="left:121px;top:86px" width="13" height="11" viewBox="0 0 13 11"><rect x=".7" y=".7" width="11.6" height="9.6" fill="none" stroke="var(--orange)" stroke-width="1.3"/><path d="M1 4h11" stroke="var(--orange)" stroke-width="1.4"/></svg>
  <svg class="abs" style="left:47px;top:136px" width="11" height="11" viewBox="0 0 11 11"><circle cx="5.5" cy="5.5" r="5" fill="var(--orange)"/><path d="M3 4l3 1-1 3" stroke="#fff" fill="none"/></svg>
  <svg class="abs" style="left:121px;top:137px" width="12" height="9" viewBox="0 0 12 9"><rect width="12" height="9" fill="var(--orange)"/><path d="M0 0l6 5 6-5" stroke="#fff" fill="none"/></svg>
  <svg class="abs" style="left:46px;top:187px" width="12" height="10" viewBox="0 0 12 10"><rect width="12" height="10" fill="var(--orange)"/><path d="M1 9l4-4 3 3 2-2 2 2" stroke="#fff" fill="none"/></svg>
  <svg class="abs" style="left:122px;top:187px" width="11" height="13" viewBox="0 0 11 13"><path d="M4 10V2l6-1v8" fill="none" stroke="var(--orange)" stroke-width="1.4"/><circle cx="2.5" cy="10.5" r="2" fill="var(--orange)"/><circle cx="8.5" cy="9" r="2" fill="var(--orange)"/></svg>
  <div class="abs" style="left:40px;top:110px;font-size:5px;line-height:1.2;text-align:center">dolor sit<br>amet</div>
  <div class="abs" style="left:116px;top:110px;font-size:5px;line-height:1.2;text-align:center">dolor sit<br>amet</div>
  <div class="abs" style="left:40px;top:160px;font-size:5px;line-height:1.2;text-align:center">dolor sit<br>amet</div>
  <div class="abs" style="left:116px;top:160px;font-size:5px;line-height:1.2;text-align:center">dolor sit<br>amet</div>
  <div class="abs" style="left:40px;top:211px;font-size:5px;line-height:1.2;text-align:center">dolor sit<br>amet</div>
  <div class="abs" style="left:116px;top:211px;font-size:5px;line-height:1.2;text-align:center">dolor sit<br>amet</div>
  <p class="abs copy" style="left:188px;top:86px;width:245px">Lorem ipsum dolor sit amet, consectetuer adipiscing elit. Aenean commodo ligula eget dolor. Aenean massa. Cum sociis natoque penatibus et magnis dis parturient montes, nascetur ridiculus mus. Donec quam felis, ultricies nec.</p>
  <p class="abs copy" style="left:188px;top:136px;width:245px">Lorem ipsum dolor sit amet, consectetuer adipiscing elit. Aenean commodo ligula eget dolor. Aenean massa. Cum sociis natoque penatibus et magnis dis parturient montes, nascetur ridiculus mus. Donec quam felis, ultricies nec, pellentesque eu, pretium.</p>
  <p class="abs copy" style="left:188px;top:187px;width:245px">Lorem ipsum dolor sit amet, consectetuer adipiscing elit. Aenean commodo ligula eget dolor. Aenean massa. Cum sociis natoque penatibus et magnis dis parturient montes, nascetur ridiculus mus. Donec quam felis, ultricies nec, pellentesque eu, pretium.</p>
  <div class="foot">Copyright © 2021 <b>Voltrix Technology, LLC.</b> All Rights Reserved.</div>
  <div class="url">www.voltrix.io | 13</div>
</section>

<section class="slide" style="left:732px;top:1290px">
  <div class="brand">VOLTRIX</div>
  <div class="dots"><i></i><i></i><i></i></div>
  <div class="photo warm" role="img" aria-label="Friends smiling together around a table" style="left:23px;top:41px;width:105px;height:90px"></div>
  <div class="photo cool" role="img" aria-label="Audience seated in a bright seminar room" style="left:130px;top:41px;width:140px;height:90px"></div>
  <div class="photo" role="img" aria-label="Team working at laptops in an open office" style="left:272px;top:41px;width:164px;height:90px"></div>
  <div class="abs" role="img" aria-label="Meeting room with colleagues, tinted in brand colours" style="left:23px;top:134px;width:213px;height:102px;background:linear-gradient(180deg,#d98a4f 0%,#8a9fbb 55%,#2f8fe6 100%)"></div>
  <div class="abs" style="left:23px;top:172px;width:213px;text-align:center;color:#fff;font-size:13px;letter-spacing:.8px;line-height:1.2">PORTOFOLIO<br>PROJECTS</div>
  <div class="abs" style="left:23px;top:218px;width:213px;text-align:center;color:#fff;font-size:4px">Presentation Powerpoint</div>
  <div class="photo warm" role="img" aria-label="Group discussing documents around a desk" style="left:238px;top:134px;width:198px;height:102px"></div>
  <div class="foot">Copyright © 2021 <b>Voltrix Technology, LLC.</b> All Rights Reserved.</div>
  <div class="url">www.voltrix.io | 14</div>
</section>

<section class="slide" style="left:1340px;top:1290px">
  <div class="brand">VOLTRIX</div>
  <div class="dots"><i></i><i></i><i></i></div>
  <div class="abs title" style="left:0;right:0;top:18px;text-align:center;font-size:14.5px">BUSINESS <span class="o">MODEL</span></div>
  <div class="abs copy" style="left:33px;top:80px;width:195px;text-align:justify">
    <p>• Lorem ipsum dolor sit amet, consectetuer adipiscing elit. Aenean commodo ligula eget dolor. Aenean massa. Cum sociis natoque penatibus et magnis dis parturient montes, nascetur ridiculus mus.</p>
    <p>• Donec quam felis, ultricies nec, pellentesque eu, pretium quis, sem. Nulla consequat massa quis enim.</p>
    <p>• Lorem ipsum dolor sit amet, consectetuer adipiscing elit. Aenean commodo ligula eget dolor.</p>
    <p>• Aenean massa. Cum sociis natoque penatibus et magnis dis parturient montes, nascetur ridiculus mus.</p>
  </div>
  <svg class="abs" style="left:240px;top:60px" width="180" height="180" viewBox="0 0 180 180" font-family="Montserrat,sans-serif" font-size="4" fill="#fff" text-anchor="middle">
    <circle cx="88" cy="88" r="84" fill="#6b7f97"/>
    <circle cx="88" cy="104" r="68" fill="#9aaabd"/>
    <circle cx="88" cy="120" r="52" fill="#3a8ee6"/>
    <circle cx="88" cy="138" r="34" fill="var(--orange)"/>
    <text x="88" y="20">Lorem ipsum</text><text x="88" y="25">dolor sit amet</text>
    <text x="88" y="53">Lorem ipsum</text><text x="88" y="58">dolor sit amet</text>
    <text x="88" y="85">Lorem ipsum</text><text x="88" y="90">dolor sit amet</text>
    <text x="88" y="135">Lorem ipsum</text><text x="88" y="140">dolor sit amet</text>
  </svg>
  <div class="foot">Copyright © 2021 <b>Voltrix Technology, LLC.</b> All Rights Reserved.</div>
  <div class="url">www.voltrix.io | 15</div>
</section>

<!-- Row 6 -->
<section class="slide" style="left:124px;top:1594px">
  <div class="brand">VOLTRIX</div>
  <div class="dots"><i></i><i></i><i></i></div>
  <div class="abs title" style="left:0;right:0;top:18px;text-align:center;font-size:14.5px">BUSINESS <span class="o">MODEL</span></div>
  <svg class="abs" style="left:70px;top:70px" width="330" height="150" viewBox="0 0 330 150" font-family="Montserrat,sans-serif">
    <path d="M180 24 C195 -8 240 -8 258 12" fill="none" stroke="#9cc8f2" stroke-width="1.2"/>
    <path d="M40 128 C60 162 115 150 130 120" fill="none" stroke="#f0a070" stroke-width="1.2"/>
    <rect x="10" y="28" width="86" height="72" rx="4" fill="#fff" stroke="#bbb"/>
    <rect x="116" y="30" width="86" height="72" rx="4" fill="#fff" stroke="#bbb"/>
    <rect x="222" y="28" width="86" height="72" rx="4" fill="#fff" stroke="#bbb"/>
    <g font-size="7.5" fill="#222">
      <text x="15" y="42">• Lorem ipsum</text><text x="21" y="51">dolor sit amet</text><text x="15" y="62">• Lorem ipsum</text><text x="21" y="71">dolor sit amet</text>
      <text x="121" y="58">• Lorem ipsum</text><text x="127" y="67">dolor sit amet</text><text x="121" y="78">• Lorem ipsum</text><text x="127" y="87">dolor sit amet</text>
      <text x="227" y="42">• Lorem ipsum</text><text x="233" y="51">dolor sit amet</text><text x="227" y="62">• Lorem ipsum</text><text x="233" y="71">dolor sit amet</text>
    </g>
    <rect x="136" y="12" width="76" height="29" rx="2" fill="var(--blue)" stroke="#fff" stroke-width="1.5"/>
    <text x="174" y="24" font-size="8.3" fill="#fff" text-anchor="middle">Lorem ipsum</text><text x="174" y="35" font-size="8.3" fill="#fff" text-anchor="middle">dolor sit amet</text>
    <rect x="28" y="90" width="76" height="29" rx="2" fill="var(--orange)" stroke="#fff" stroke-width="1.5"/>
    <text x="66" y="102" font-size="8.3" fill="#fff" text-anchor="middle">Lorem ipsum</text><text x="66" y="113" font-size="8.3" fill="#fff" text-anchor="middle">dolor sit amet</text>
    <rect x="242" y="90" width="76" height="29" rx="2" fill="var(--slate)" stroke="#fff" stroke-width="1.5"/>
    <text x="280" y="102" font-size="8.3" fill="#fff" text-anchor="middle">Lorem ipsum</text><text x="280" y="113" font-size="8.3" fill="#fff" text-anchor="middle">dolor sit amet</text>
  </svg>
  <div class="foot">Copyright © 2021 <b>Voltrix Technology, LLC.</b> All Rights Reserved.</div>
  <div class="url">www.voltrix.io | 16</div>
</section>

<section class="slide" style="left:732px;top:1594px">
  <div class="brand">VOLTRIX</div>
  <div class="dots"><i></i><i></i><i></i></div>
  <div class="abs title" style="left:0;right:0;top:18px;text-align:center;font-size:14.5px">BUSINESS <span class="o">MODEL</span></div>
  <div class="abs copy" style="left:37px;top:70px;width:130px;text-align:justify">
    <p>• Lorem ipsum dolor sit amet, consectetuer adipiscing elit. Aenean commodo ligula eget dolor.</p>
    <p>• Aenean massa. Cum sociis natoque penatibus et magnis dis parturient montes, nascetur ridiculus mus.</p>
    <p>• Donec quam felis, ultricies nec, pellentesque eu, pretium quis, sem. Nulla consequat massa quis enim.</p>
    <p>• Lorem ipsum dolor sit amet, consectetuer adipiscing elit. Aenean</p>
  </div>
  <svg class="abs" style="left:185px;top:58px" width="260" height="160" viewBox="0 0 260 160" font-family="Montserrat,sans-serif">
    <text x="130" y="14" font-size="7" fill="#666" text-anchor="middle">Chart Title</text>
    <g stroke="#e4e4e4" stroke-width=".6">
      <line x1="20" y1="26" x2="252" y2="26"/><line x1="20" y1="43" x2="252" y2="43"/><line x1="20" y1="59" x2="252" y2="59"/><line x1="20" y1="76" x2="252" y2="76"/><line x1="20" y1="92" x2="252" y2="92"/><line x1="20" y1="109" x2="252" y2="109"/><line x1="20" y1="125" x2="252" y2="125"/>
    </g>
    <g font-size="4.8" fill="#777" text-anchor="end">
      <text x="12" y="28">6</text><text x="12" y="45">5</text><text x="12" y="61">4</text><text x="12" y="78">3</text><text x="12" y="94">2</text><text x="12" y="111">1</text><text x="12" y="127">0</text>
    </g>
    <g>
      <rect x="34" y="53" width="6" height="72" fill="var(--orange)"/><rect x="41" y="85" width="6" height="40" fill="var(--blue)"/><rect x="48" y="92" width="6" height="33" fill="#a7b5c3"/>
      <rect x="92" y="83" width="6" height="42" fill="var(--orange)"/><rect x="99" y="52" width="6" height="73" fill="var(--blue)"/><rect x="106" y="92" width="6" height="33" fill="#a7b5c3"/>
      <rect x="150" y="67" width="6" height="58" fill="var(--orange)"/><rect x="157" y="96" width="6" height="29" fill="var(--blue)"/><rect x="164" y="76" width="6" height="49" fill="#a7b5c3"/>
      <rect x="208" y="51" width="6" height="74" fill="var(--orange)"/><rect x="215" y="79" width="6" height="46" fill="var(--blue)"/><rect x="222" y="43" width="6" height="82" fill="#a7b5c3"/>
    </g>
    <g font-size="4.8" fill="#777" text-anchor="middle">
      <text x="44" y="136">Category 1</text><text x="102" y="136">Category 2</text><text x="160" y="136">Category 3</text><text x="218" y="136">Category 4</text>
    </g>
    <g font-size="4.6" fill="#777">
      <rect x="81" y="146" width="3" height="3" fill="var(--orange)"/><text x="86" y="149.5">Series 1</text>
      <rect x="115" y="146" width="3" height="3" fill="var(--blue)"/><text x="120" y="149.5">Series 2</text>
      <rect x="149" y="146" width="3" height="3" fill="#a7b5c3"/><text x="154" y="149.5">Series 3</text>
    </g>
  </svg>
  <div class="foot">Copyright © 2021 <b>Voltrix Technology, LLC.</b> All Rights Reserved.</div>
  <div class="url">www.voltrix.io | 17</div>
</section>

<section class="slide" style="left:1340px;top:1594px">
  <div class="brand">VOLTRIX</div>
  <div class="dots"><i></i><i></i><i></i></div>
  <div class="band" style="left:365px;top:0;width:103px;height:264px"></div>
  <div class="photo warm framed" role="img" aria-label="Two colleagues reviewing documents together" style="left:233px;top:30px;width:136px;height:206px"></div>
  <div class="abs title" style="left:45px;top:58px">CONTACT <span class="o">US</span></div>
  <div class="abs" style="left:40px;top:118px;font-size:6px">FAX</div>
  <div class="abs copy" style="left:40px;top:126px">+555014820</div>
  <div class="abs" style="left:110px;top:118px;font-size:6px">Number Office</div>
  <div class="abs copy" style="left:110px;top:126px;white-space:nowrap">+5550173926 &nbsp;+5550173927</div>
  <div class="abs" style="left:40px;top:150px;font-size:6px">Address</div>
  <div class="abs copy" style="left:40px;top:164px;line-height:1.9">458 Lorem ipsum<br>1203 dolor sit amet.</div>
  <div class="abs" style="left:113px;top:150px;font-size:6px">Email</div>
  <div class="abs copy" style="left:113px;top:164px">hello@voltrix.io</div>
  <div class="foot">Copyright © 2021 <b>Voltrix Technology, LLC.</b> All Rights Reserved.</div>
</section>

</div>
</body>
</html>
```